PowerPoint Template for Regional Harmony Institute. Website is www.regionalharmonyinstitute.com

The tagline for the Center is "Connecting the brightest minds in healthcare"

```html
<!DOCTYPE html>
<html lang="en">
<head>
<meta charset="utf-8">
<title>Regional Harmony Institute – Presentation Template</title>
<link href="https://fonts.googleapis.com/css2?family=Montserrat:wght@500;600;700&display=swap" rel="stylesheet">
<style>
  :root {
    --backdrop: #dcdcdc;
    --slide: #ffffff;
    --navy: #0d4a7a;
    --blue: #0a86cf;
    --blue-light: #4fb0e0;
    --blue-dark: #0b3f6b;
    --rule: #9cc8e6;
    --red: #e8141b;
    --ink: #111111;
    --image-a: #dfe4ea;
    --image-b: #f2f4f6;
  }
  * { box-sizing: border-box; margin: 0; padding: 0; }
  html, body { width: 1200px; height: 900px; overflow: hidden; }
  body {
    background: var(--backdrop);
    font-family: "Montserrat", Arial, sans-serif;
    position: relative;
  }
  .slide {
    position: absolute;
    width: 277px;
    height: 206px;
    background: var(--slide);
    border-bottom: 4px solid var(--blue);
    overflow: hidden;
  }
  .row-1 { top: 246px; }
  .row-2 { top: 475px; }
  .col-1 { left: 13px; }
  .col-2 { left: 312px; }
  .col-3 { left: 612px; }
  .col-4 { left: 908px; }

  .brand {
    position: absolute; top: 90px; left: 0; right: 0;
    display: flex; align-items: center; justify-content: center; gap: 6px;
    color: var(--navy); font-weight: 600; font-size: 11px;
  }
  .brand-dot { width: 14px; height: 14px; border-radius: 50%; background: var(--navy); }

  .title-centered {
    position: absolute; left: 0; right: 0;
    display: flex; align-items: center; justify-content: center; gap: 5px;
    color: var(--navy); font-weight: 600; font-size: 11.5px;
  }
  .title-centered::before {
    content: ""; width: 16px; height: 1.5px; background: var(--blue);
  }
  .title-left {
    position: absolute; top: 30px; left: 29px; right: 0;
    color: var(--navy); font-weight: 600; font-size: 11.5px;
    padding-bottom: 3px; border-bottom: 1px solid var(--rule);
  }
  .body-text {
    position: absolute; left: 20px; right: 20px;
    text-align: center; color: var(--ink);
    font-weight: 600; font-size: 6.4px; line-height: 1.35;
  }
  .button {
    position: absolute; top: 142px; left: 50%; transform: translateX(-50%);
    width: 94px; height: 16px; border: 1px solid var(--navy);
    color: var(--navy); font-weight: 700; font-size: 7.5px;
    display: flex; align-items: center; justify-content: center;
  }
  .hero-image {
    position: absolute; top: 19px; left: 0; right: 0; height: 120px;
    background: linear-gradient(90deg, var(--image-a), var(--image-b) 55%, var(--image-a));
  }
  .short-rule {
    position: absolute; left: 50%; transform: translateX(-50%);
    width: 14px; height: 1px; background: var(--rule);
  }
  .bullets {
    position: absolute; top: 68px; left: 49px; list-style: none;
    font-size: 6.3px; font-weight: 600; color: var(--ink);
  }
  .bullets li { height: 13px; position: relative; padding-left: 9px; }
  .bullets li::before {
    content: ""; position: absolute; left: 0; top: 2px;
    width: 2px; height: 2px; background: var(--red);
  }
  .tag {
    position: absolute; top: 141px; left: 36px; width: 200px; height: 16px;
    border: 1px solid #9a9a9a; display: flex; align-items: center;
    font-size: 6.3px; font-weight: 700;
  }
  .tag-label {
    height: 100%; width: 60px; background: var(--red); color: #fff;
    display: flex; align-items: center; padding-left: 5px;
    clip-path: polygon(0 0, 88% 0, 100% 50%, 88% 100%, 0 100%);
  }
  .tag-text { padding-left: 9px; color: var(--ink); }
  .pie { position: absolute; top: 0; left: 0; }
  .long-text {
    position: absolute; top: 74px; left: 44px; right: 44px;
    text-align: center; font-size: 6.2px; font-weight: 600; line-height: 1.3; color: var(--ink);
  }
</style>
</head>
<body>

<section class="slide row-1 col-1" aria-label="Cover slide">
  <div class="brand"><span class="brand-dot"></span><span>Regional Harmony Institute</span></div>
</section>

<section class="slide row-1 col-2" aria-label="Section title slide">
  <h2 class="title-centered" style="top:90px">Regional Harmony Institute</h2>
</section>

<section class="slide row-1 col-3" aria-label="Title with call to action">
  <h2 class="title-centered" style="top:54px">Regional Harmony Institute</h2>
  <p class="body-text" style="top:95px">Lorem ipsum dolor sit amet, consectetuer adipiscing elit, sed diam nonummy nibh euismod tincidunt ut laoreet dolore magna</p>
  <div class="button">Lorem ipsum</div>
</section>

<section class="slide row-1 col-4" aria-label="Image slide">
  <div class="hero-image" role="img" aria-label="Illustration of a network hub linking healthcare icons over a map"></div>
  <span class="short-rule" style="top:152px"></span>
  <p class="body-text" style="top:157px">Lorem ipsum dolor sit amet, consectetuer adipiscing elit, sed diam nonummy nibh euismod tincidunt ut laoreet dolore magna</p>
</section>

<section class="slide row-2 col-1" aria-label="Bullet list slide">
  <h2 class="title-left">Regional Harmony Institute</h2>
  <ul class="bullets">
    <li>Lorem ipsum dolor sit amet, consectetuer adipiscing elit</li>
    <li>Sed diam nonummy nibh euismod</li>
    <li>Tincidunt ut laoreet dolore magna</li>
    <li>Dolor sit amet, consectetuer adipiscing elit</li>
    <li>Sed diam nonummy nibh euismod</li>
    <li>Tincidunt ut laoreet dolore magna</li>
  </ul>
</section>

<section class="slide row-2 col-2" aria-label="Highlight slide">
  <h2 class="title-centered" style="top:54px">Regional Harmony Institute</h2>
  <p class="body-text" style="top:95px">Lorem ipsum dolor sit amet, consectetuer adipiscing elit, sed diam nonummy nibh euismod tincidunt ut laoreet dolore magna</p>
  <div class="tag"><span class="tag-label">Lorem ipsum</span><span class="tag-text">Sed diam nonummy nibh euismod</span></div>
</section>

<section class="slide row-2 col-3" aria-label="Chart slide">
  <h2 class="title-left">Regional Harmony Institute</h2>
  <svg class="pie" width="277" height="206" viewBox="0 0 277 206" aria-label="Pie chart">
    <circle cx="138" cy="111" r="49" fill="var(--blue)"/>
    <path d="M138 111 L138 62 A49 49 0 0 1 158.7 66.6 Z" fill="var(--blue-dark)"/>
    <path d="M138 111 L158.7 66.6 A49 49 0 0 1 181.3 88 Z" fill="var(--blue-light)"/>
  </svg>
  <p class="body-text" style="top:170px">Lorem ipsum dolor sit amet, consectetuer adipiscing elit, sed diam nonummy nibh euismod tincidunt ut laoreet dolore magna</p>
</section>

<section class="slide row-2 col-4" aria-label="Text slide">
  <span class="short-rule" style="top:72px"></span>
  <p class="long-text">Lorem ipsum dolor sit amet, consectetuer adipiscing elit, sed diam nonummy nibh euismod tincidunt ut laoreet dolore magna aliquam erat volutpat. Ut wisi enim ad minim veniam, quis nostrud exerci tation ullamcorper suscipit lobortis nisl ut aliquip ex ea commodo consequat. Duis autem vel eum iriure dolor in hendrerit in vulputate velit esse molestie consequat, vel illum dolore eu feugiat nulla facilisis at vero eros et accumsan et iusto odio dignissim qui blandit praesent luptatum zzril delenit augue duis</p>
  <span class="short-rule" style="top:142px"></span>
</section>

</body>
</html>
```